The Plasterline & Soundcraft Partners Inc (PSPI)

Create a LOGO and Business Card design.

Colors: Black, Bright Yellow & Red

Description of company: commercial carpentry, metal framing, drywall, taping/spackling, demolition, rough/finish carpentry.

Target Market(s)

developers, architects, general contractors, construction managers

Industry/Entity Type

Business

```html
<!DOCTYPE html>
<html lang="en">
<head>
<meta charset="utf-8">
<title>PSPI Business Card</title>
<link rel="stylesheet" href="https://fonts.googleapis.com/css2?family=Arimo:wght@400;700&display=swap">
<style>
  :root {
    --board-light: #dcdcdc;
    --board-mid: #c4c4c4;
    --board-dark: #a9a9a9;
    --ink: #111111;
    --brand-yellow: #ffef00;
    --brand-red: #e50000;
  }
  html, body {
    margin: 0;
    padding: 0;
    width: 1200px;
    height: 720px;
    overflow: hidden;
    background: #ffffff;
  }
  .card {
    position: relative;
    width: 1200px;
    height: 720px;
    overflow: hidden;
    font-family: "Arimo", Arial, sans-serif;
    color: var(--ink);
  }
  .card__backdrop {
    position: absolute;
    inset: 0;
    background:
      radial-gradient(ellipse at 30% 40%, var(--board-light) 0%, transparent 60%),
      linear-gradient(160deg, var(--board-mid) 0%, var(--board-light) 45%, var(--board-mid) 75%, var(--board-dark) 100%);
  }
  .brand {
    position: absolute;
    left: 0;
    top: 0;
    width: 1200px;
    height: 400px;
    text-align: center;
  }
  .brand__mark {
    position: absolute;
    left: 0;
    right: 0;
    top: 62px;
    margin: 0;
    font-weight: 700;
    font-size: 340px;
    line-height: 340px;
    letter-spacing: 4px;
    color: var(--brand-red);
  }
  .brand__name {
    position: absolute;
    left: 0;
    right: 0;
    top: 188px;
    margin: 0;
    font-weight: 700;
    font-size: 58px;
    line-height: 62px;
    white-space: nowrap;
    color: var(--brand-yellow);
    -webkit-text-stroke: 5px var(--ink);
    paint-order: stroke fill;
  }
  .contact {
    position: absolute;
    left: 35px;
    top: 438px;
  }
  .contact__name {
    margin: 0;
    font-weight: 400;
    font-size: 86px;
    line-height: 92px;
    text-shadow: 2px 4px 4px rgba(0,0,0,0.4);
  }
  .contact__details {
    list-style: none;
    margin: 4px 0 0;
    padding: 0;
    font-size: 34px;
    line-height: 50px;
  }
</style>
</head>
<body>
  <main class="card">
    <div class="card__backdrop" role="img" aria-label="Close-up of taped and spackled drywall panels in soft greys"></div>

    <header class="brand">
      <p class="brand__mark">PSPI</p>
      <h1 class="brand__name">Plasterline and Soundcraft Partners, Inc</h1>
    </header>

    <section class="contact">
      <h2 class="contact__name">Sam Carter.</h2>
      <ul class="contact__details">
        <li class="contact__phone">555-555-0142</li>
        <li class="contact__web">www.plasterline.com.au</li>
        <li class="contact__email">sam@plasterline.com.au</li>
      </ul>
    </section>
  </main>
</body>
</html>
```